Building Company Business Card Design

I am looking to get a business card designed for my Building Company. Please find the logo attached.

Industry/Entity Type

Business

Contact Information for Business Card

Mobile 0472 913 046
Email admin@tarrowconstructworks.com.au
Website www.tarrowconstructworks.com.au

Colors
0255a3

```html
<!DOCTYPE html>
<html lang="en">
<head>
<meta charset="utf-8">
<title>Tarrow Construct Works – Business Card</title>
<link rel="stylesheet" href="https://fonts.googleapis.com/css2?family=Montserrat:wght@600;700&family=Open+Sans:wght@400&display=swap">
<style>
  :root {
    --brand-blue: #0255a3;
    --deep-blue: #003a8c;
    --navy: #15305e;
    --ink: #2b2b2b;
    --paper: #ffffff;
    --backdrop: #0c0c0e;
  }
  * { box-sizing: border-box; margin: 0; padding: 0; }
  html, body { width: 1200px; height: 1200px; overflow: hidden; background: var(--backdrop); }
  .canvas {
    width: 1200px; height: 1200px;
    display: flex; flex-direction: column; align-items: center; justify-content: center; gap: 50px;
  }
  .card {
    position: relative; width: 860px; height: 525px; overflow: hidden;
    border-radius: 4px;
  }
  .card-front { background: var(--paper); }
  .card-front .wave { position: absolute; inset: 0; width: 100%; height: 100%; }
  .contact {
    position: absolute; left: 70px; top: 90px;
    font-family: "Open Sans", sans-serif; color: var(--ink);
  }
  .contact .name {
    font-family: "Montserrat", sans-serif; font-weight: 700; font-size: 30px;
    color: var(--brand-blue); letter-spacing: 0.5px;
  }
  .contact .role { font-size: 19px; margin-top: 2px; margin-bottom: 26px; }
  .contact ul { list-style: none; }
  .contact li { display: flex; align-items: center; gap: 14px; font-size: 19px; line-height: 36px; }
  .contact svg { width: 20px; height: 20px; fill: var(--brand-blue); flex: none; }
  .wordmark {
    position: absolute; font-family: "Montserrat", sans-serif; font-weight: 700;
    text-transform: uppercase; line-height: 1.05; text-align: center;
  }
  .card-front .wordmark { right: 60px; top: 120px; font-size: 40px; color: var(--brand-blue); }
  .card-back {
    background: radial-gradient(ellipse at 45% 40%, #0a5bc0 0%, var(--brand-blue) 35%, var(--deep-blue) 100%);
  }
  .card-back .wordmark {
    left: 0; right: 0; top: 50%; transform: translateY(-50%);
    font-size: 58px; color: var(--paper);
  }
</style>
</head>
<body>
<main class="canvas">
  <section class="card card-front" aria-label="Business card front">
    <svg class="wave" viewBox="0 0 860 525" preserveAspectRatio="none" aria-hidden="true">
      <path d="M0 322 C150 350 300 400 420 470 L440 482 L0 345 Z" fill="var(--navy)"/>
      <path d="M0 352 C150 380 300 430 400 490 L430 505 L0 368 Z" fill="var(--brand-blue)"/>
      <path d="M430 525 C460 470 480 455 520 450 C620 445 760 470 860 500 L860 525 Z" fill="var(--brand-blue)"/>
    </svg>
    <div class="contact">
      <p class="name">JOHN DOE</p>
      <p class="role">Director</p>
      <ul>
        <li><svg viewBox="0 0 24 24"><path d="M6.6 10.8a15 15 0 0 0 6.6 6.6l2.2-2.2a1 1 0 0 1 1-.25 11.4 11.4 0 0 0 3.6.57 1 1 0 0 1 1 1V20a1 1 0 0 1-1 1A17 17 0 0 1 3 4a1 1 0 0 1 1-1h3.5a1 1 0 0 1 1 1c0 1.25.2 2.45.57 3.6a1 1 0 0 1-.25 1z"/></svg>0472 913 046</li>
        <li><svg viewBox="0 0 24 24"><rect x="2" y="5" width="20" height="14" rx="1"/></svg>www.tarrowconstructworks.com.au</li>
        <li><svg viewBox="0 0 24 24"><circle cx="12" cy="12" r="10"/></svg>admin@tarrowconstructworks.com.au</li>
      </ul>
    </div>
    <p class="wordmark">Tarrow<br>Construct Works</p>
  </section>

  <section class="card card-back" aria-label="Business card back">
    <p class="wordmark">Tarrow<br>Construct Works</p>
  </section>
</main>
</body>
</html>
```